RM Cargoline businesscard project

RM Cargoline Ltd is a freshly founded small (3 employees), young (average age is 30 years) company, living from the road transportation market without own tools.
We would like to have an impressive, new-line, cool busines card for a freshly founded forwarding company on an overcrowded market which raises attention and makes the potential partners eager to work with us.

Target Market(s)

The main profile of the company is logistic/forwarding on road.

Industry/Entity Type

Freight Forwarding

Contact Information for Business Card

Name: Berki Zsófia
Title: general manager
mobile nr: +36-70/482-5193
fax nr: +36-1/534-9061
e-mail: zsofia.berki@rmcargoline.example
info@rmcargoline.example
website address: http://www.rmcargoline.example
and if possible maybe some funny or helpful info on the back

Requirements
Must have
• contact details above
Nice to have
• some really nice and catching back-side (info, graphics, useful tool info... anything)
Should not have
• trucks, road, ship, airplane on it...

```html
<!DOCTYPE html>
<html lang="en">
<head>
<meta charset="utf-8">
<title>RM Cargoline – Business Card</title>
<link rel="stylesheet" href="https://fonts.googleapis.com/css2?family=Source+Sans+3:wght@400;600&display=swap">
<style>
  :root {
    --canvas: #ffffff;
    --band: #98444f;
    --band-light: #b6646e;
    --sky: #cfe9fa;
    --paper: #ffffff;
    --ink: #333333;
    --brand-ink: #2a2a2a;
    --brand: #2e6aa6;
    --brand-faint: #b5ddf6;
    --on-band: #ffffff;
  }
  html, body {
    margin: 0;
    width: 1200px;
    height: 1000px;
    overflow: hidden;
    background: var(--canvas);
    font-family: "Source Sans 3", "Myriad Pro", Arial, sans-serif;
  }
  .card {
    position: absolute;
    width: 420px;
    height: 238px;
    background: var(--paper);
    box-shadow: 3px 4px 7px rgba(0, 0, 0, 0.35);
    overflow: hidden;
  }
  .card--front { left: 298px; top: 212px; }
  .card--back  { left: 550px; top: 540px; }

  .card__art { position: absolute; inset: 0; }

  .band-text {
    position: absolute;
    left: 0; right: 0;
    text-align: center;
    color: var(--on-band);
    font-size: 15.5px;
    letter-spacing: 0.2px;
  }
  .band-text--top { top: 7px; }
  .band-text--bottom { top: 213px; }

  .person { position: absolute; left: 19px; top: 93px; color: var(--ink); }
  .person__name { font-size: 20px; line-height: 24px; }
  .person__title { font-size: 13.5px; line-height: 18px; }

  .brand {
    position: absolute;
    top: 78px;
    display: flex;
    flex-direction: column;
    align-items: center;
    gap: 12px;
  }
  .brand__square { width: 44px; height: 44px; }
  .brand__name { font-size: 19px; font-weight: 600; line-height: 1; white-space: nowrap; }

  .brand--front { left: 145px; width: 130px; }
  .brand--front .brand__square { background: var(--brand); }
  .brand--front .brand__name { color: var(--brand-ink); }

  .brand--back { left: 0; width: 420px; }
  .brand--back .brand__square { background: var(--brand-faint); }
  .brand--back .brand__name { color: var(--brand-faint); }

  .contact {
    position: absolute;
    left: 274px;
    top: 67px;
    margin: 0;
    color: var(--ink);
    font-size: 12.5px;
    line-height: 14.5px;
    white-space: nowrap;
  }
  .contact dt { margin: 0; }
  .contact dd { margin: 0 0 7px 0; }
</style>
</head>
<body>

<section class="card card--front" aria-label="Business card front">
  <svg class="card__art" viewBox="0 0 420 238" width="420" height="238" aria-hidden="true">
    <defs>
      <linearGradient id="paperGlow" x1="0" x2="1" y1="0" y2="0">
        <stop offset="0" stop-color="var(--sky)"/>
        <stop offset="0.3" stop-color="#ffffff"/>
        <stop offset="0.7" stop-color="#ffffff"/>
        <stop offset="1" stop-color="var(--sky)"/>
      </linearGradient>
      <linearGradient id="bandTop" x1="0" x2="0" y1="0" y2="1">
        <stop offset="0" stop-color="var(--band)"/>
        <stop offset="0.75" stop-color="var(--band)"/>
        <stop offset="1" stop-color="var(--band-light)"/>
      </linearGradient>
      <linearGradient id="bandBottom" x1="0" x2="0" y1="1" y2="0">
        <stop offset="0" stop-color="var(--band)"/>
        <stop offset="0.75" stop-color="var(--band)"/>
        <stop offset="1" stop-color="var(--band-light)"/>
      </linearGradient>
    </defs>
    <rect class="card__paper" width="420" height="238" fill="url(#paperGlow)"/>
    <path class="card__band-top" d="M0 0 H420 V24 Q210 40 0 24 Z" fill="url(#bandTop)"/>
    <path class="card__band-bottom" d="M0 238 H420 V219 Q210 193 0 219 Z" fill="url(#bandBottom)"/>
  </svg>

  <div class="band-text band-text--top">www.rmcargoline.example</div>

  <div class="person">
    <div class="person__name">Berki Zsófia</div>
    <div class="person__title">General Manager</div>
  </div>

  <div class="brand brand--front">
    <span class="brand__square"></span>
    <span class="brand__name">RM Cargoline</span>
  </div>

  <dl class="contact">
    <dt>phone:</dt><dd>+36-70/482-5193</dd>
    <dt>fax:</dt><dd>+36-1/534-9061</dd>
    <dt>mail:</dt><dd>info@rmcargoline.example</dd>
  </dl>

  <div class="band-text band-text--bottom">zsofia.berki@rmcargoline.example</div>
</section>

<section class="card card--back" aria-label="Business card back">
  <div class="brand brand--back">
    <span class="brand__square"></span>
    <span class="brand__name">RM Cargoline</span>
  </div>
</section>

</body>
</html>
```